Organic, colorful clean label design my handmade sugar scrubs company

Hi! I am creating a label to place on my body scrubs that I am selling. I had a logo made already through PixelHarbor and have attached it for reference in color scale and in black. My logo is based off of a sunflower so I want the label to tie in with the logo. I have placed blanks on the label and numbered them. I have attached a list with the words that will be included on this label. The size of my label on the jar will be 2.25x8.75inches. I drew my sketch close to this scale.

Target Market(s)

young adults-adults, great as a gift or for personal use in the shower

Industry/Entity Type

Health And Wellness

Font styles to use
Serif
Script

Colors

Designer to choose colors to be used in the design.

Requirements
Must have
• I would like the color scheme and some elements of the design to tie in together, as the logo will be a separate sticker on the lid of the jar. I have sketched up a draft of my label. In the center, I have the front of the label, with the title, list of ingredients etc. On either side will be the directions and the warnings. I want the flowers to be sunflowers. I want the label to look colorful, appealing and natural looking.
Nice to have
• When writing points number 4, 6-8, I think it would look nice if they were in boxes. The label has flowers on it, but I also don't want it to look overly feminine. Something natural but neutral is good so a man wouldn't be embarrassed to have this in his shower.

```html
<!DOCTYPE html>
<html lang="en">
<head>
<meta charset="utf-8">
<title>Handmade Sugar Scrubs – Jar Label</title>
<link href="https://fonts.googleapis.com/css2?family=Questrial&family=Pinyon+Script&display=swap" rel="stylesheet">
<style>
  :root {
    --backdrop: #ead6cf;
    --label-white: #ffffff;
    --ink: #3b3b3b;
    --olive: #6f7f1f;
    --olive-line: #8a9a2c;
    --box-border: #9aa8b4;
    --sun-yellow: #f7d21c;
    --sun-orange: #f2a81d;
    --leaf-green: #8cc04a;
    --swirl-blue: #c9d6df;
  }
  * { margin: 0; padding: 0; box-sizing: border-box; }
  html, body { width: 1200px; height: 1200px; overflow: hidden; }
  body {
    background: var(--backdrop);
    font-family: "Questrial", "Century Gothic", sans-serif;
    color: var(--ink);
    position: relative;
  }
  .label {
    position: absolute;
    left: 20px;
    top: 462px;
    width: 1160px;
    height: 276px;
    background: var(--label-white);
    overflow: hidden;
  }
  .floral {
    position: absolute;
    top: 0;
    height: 100%;
  }
  .floral--left {
    left: 0;
    width: 470px;
    background:
      radial-gradient(circle at 12% 22%, var(--sun-orange) 0 9%, transparent 16%),
      radial-gradient(circle at 88% 24%, var(--sun-orange) 0 9%, transparent 17%),
      radial-gradient(circle at 82% 78%, var(--sun-orange) 0 10%, transparent 18%),
      radial-gradient(circle at 10% 86%, var(--sun-orange) 0 8%, transparent 15%),
      linear-gradient(135deg, #fbe67a 0%, #eaf3d6 45%, #e2ecef 70%, #fbe67a 100%);
  }
  .floral--right {
    right: 0;
    width: 440px;
    background:
      radial-gradient(circle at 14% 24%, var(--sun-orange) 0 9%, transparent 17%),
      radial-gradient(circle at 18% 80%, var(--sun-orange) 0 10%, transparent 18%),
      radial-gradient(circle at 92% 22%, var(--sun-orange) 0 8%, transparent 15%),
      radial-gradient(circle at 90% 86%, var(--sun-orange) 0 9%, transparent 16%),
      linear-gradient(225deg, #fbe67a 0%, #e2ecef 35%, #eaf3d6 60%, #fbe67a 100%);
  }
  .front-panel {
    position: absolute;
    left: 450px;
    width: 280px;
    top: 0;
    height: 100%;
    background: var(--label-white);
    box-shadow: 0 0 24px 18px var(--label-white);
    text-align: center;
  }
  .brand {
    position: absolute;
    top: 44px;
    left: 0;
    right: 0;
    display: flex;
    justify-content: center;
    align-items: center;
    gap: 8px;
    font-size: 17px;
    color: var(--olive);
    letter-spacing: 0.5px;
  }
  .brand-dot {
    width: 12px;
    height: 12px;
    border-radius: 50%;
    background: var(--sun-yellow);
  }
  .product-title {
    position: absolute;
    top: 100px;
    left: -40px;
    right: -40px;
    font-family: "Pinyon Script", cursive;
    font-weight: 400;
    font-size: 34px;
    color: var(--olive);
    white-space: nowrap;
  }
  .divider {
    position: absolute;
    top: 189px;
    left: 12px;
    right: 12px;
    height: 2px;
    background: var(--olive-line);
  }
  .ingredients {
    position: absolute;
    top: 198px;
    left: -20px;
    right: -20px;
    font-size: 10.5px;
    line-height: 1.45;
  }
  .net-weight {
    position: absolute;
    top: 250px;
    left: 0;
    right: 0;
    font-size: 11.5px;
  }
  .info-box {
    position: absolute;
    top: 64px;
    height: 172px;
    background: var(--label-white);
    border: 1.5px solid var(--box-border);
    border-radius: 8px;
    text-align: center;
    padding: 14px 10px;
  }
  .info-box--directions { left: 82px; width: 244px; }
  .info-box--warnings { left: 848px; width: 246px; top: 64px; height: 172px; padding: 8px 8px; }
  .directions {
    font-size: 13px;
    line-height: 1.42;
  }
  .box-rule {
    width: 180px;
    height: 2px;
    background: var(--olive-line);
    margin: 20px auto 10px;
  }
  .maker-note {
    font-size: 10.5px;
    line-height: 1.45;
  }
  .warnings {
    font-size: 11.5px;
    line-height: 1.44;
  }
</style>
</head>
<body>
  <section class="label">
    <div class="floral floral--left" role="img" aria-label="Sunflower illustrations with green leaves and pale blue spirals"></div>
    <div class="floral floral--right" role="img" aria-label="Sunflower illustrations with green leaves and pale blue spirals"></div>

    <div class="info-box info-box--directions">
      <p class="directions">Directions: Gently scrub the desired amount onto skin during shower routine. Rinse and towel dry. Enjoy perfectly hydrated skin.</p>
      <div class="box-rule"></div>
      <p class="maker-note">Handmade in Miami, Florida.<br>Direct questions or concerns to<br>hello@goldengrovescrubs.com.</p>
    </div>

    <div class="front-panel">
      <div class="brand"><span class="brand-dot"></span>Golden Grove</div>
      <h1 class="product-title">Handmade Sugar Scrubs</h1>
      <div class="divider"></div>
      <p class="ingredients">Ingredients: Organic Sugar, Organic Coconut Oil,<br>Organic Shea Nut Butter, Almond Oil,<br>Vitamin E Oil, Organic Beeswax, Essential Oils.</p>
      <p class="net-weight">Net Wt. 8oz</p>
    </div>

    <div class="info-box info-box--warnings">
      <p class="warnings">Contains tree nuts (shea nut butter). Not tested on animals. Do not eat. For external use only. Do not apply to broken skin. Discontinue use if irritation occurs. May make shower slippery. Use at your own discretion. By purchasing this product, you agree to use this product only for the intended use and waive all responsibility from Golden Grove, LLC.</p>
    </div>
  </section>
</body>
</html>
```